mobile app - telecom industry

We are a tech/service company. Our product is a mobile application for physical site inspection called “Verko”. Our target industry is telecommunica...

Target Market(s)

telecommunication

Industry/Entity Type

Industry

Requirements
Must have
• Screen size Orbix 7 - Android
• Suggest 3 colors
• Design 9 pages

```html
<!DOCTYPE html>
<html lang="en">
<head>
<meta charset="utf-8">
<title>Verko – Closed Work Orders</title>
<link rel="stylesheet" href="https://fonts.googleapis.com/css2?family=Open+Sans:wght@300;400&display=swap">
<style>
  :root {
    --teal: #48b3a8;
    --teal-text: #3aaea2;
    --row-grey: #bbbbbb;
    --row-line: #cdcdcd;
    --white: #ffffff;
    --divider: #eeeeee;
    --plus-border: #c9c9c9;
    --plus-stroke: #b5b5b5;
  }
  * { box-sizing: border-box; margin: 0; padding: 0; }
  html, body { width: 1200px; height: 1200px; overflow: hidden; }
  body {
    background: var(--white);
    font-family: "Open Sans", Arial, sans-serif;
    position: relative;
  }
  .page-label {
    position: absolute;
    left: 52px; top: 536px;
    color: var(--teal);
    font-size: 39px;
    font-weight: 400;
    line-height: 1.1;
  }
  .screen {
    position: absolute;
    left: 398px; top: 251px;
    width: 406px; height: 718px;
    background: var(--white);
    box-shadow: 0 0 0 1px #e4e4e4;
    overflow: hidden;
  }
  .app-bar {
    height: 70px;
    background: var(--teal);
    color: var(--white);
    position: relative;
  }
  .status-bar {
    height: 19px;
    display: flex; align-items: center; justify-content: space-between;
    padding: 0 6px 0 5px;
    font-size: 10px; font-weight: 300;
  }
  .status-left, .status-right { display: flex; align-items: center; gap: 4px; }
  .battery { width: 26px; height: 7px; background: var(--white); border-radius: 1px; }
  .nav { display: flex; align-items: center; height: 51px; padding-left: 20px; gap: 14px; }
  .brand { font-size: 24px; font-weight: 300; letter-spacing: 0.5px; }
  .section-title {
    height: 51px;
    display: flex; align-items: center; justify-content: center;
    color: var(--teal-text);
    font-size: 18px; font-weight: 300;
    border-bottom: 1px solid var(--divider);
  }
  .order {
    position: absolute; left: 12px;
    width: 302px; height: 62px;
    background: var(--row-grey);
    color: var(--white);
    font-weight: 300;
    font-size: 18px;
  }
  .order-line {
    height: 31px;
    display: flex; align-items: center; justify-content: space-between;
    padding: 0 17px 0 11px;
  }
  .order-line:first-child { border-bottom: 1px solid var(--row-line); }
  .delete-btn {
    position: absolute; left: 330px;
    width: 62px; height: 62px;
    background: var(--teal);
    border-radius: 7px;
    display: flex; align-items: center; justify-content: center;
  }
  .list-end {
    position: absolute; left: 0; top: 530px; width: 100%;
    border-top: 1px solid var(--divider);
  }
  .add-btn {
    position: absolute; left: 171px; top: 546px;
    width: 63px; height: 63px;
    border: 1px solid var(--plus-border);
    border-radius: 6px;
    display: flex; align-items: center; justify-content: center;
  }
</style>
</head>
<body>
  <h1 class="page-label">Close Work Order<br>Page</h1>

  <main class="screen">
    <header class="app-bar">
      <div class="status-bar">
        <div class="status-left">
          <svg width="36" height="6" viewBox="0 0 36 6"><g fill="#fff"><circle cx="3" cy="3" r="2.8"/><circle cx="10" cy="3" r="2.8"/><circle cx="17" cy="3" r="2.8"/><circle cx="24" cy="3" r="2.8"/><circle cx="31" cy="3" r="2.8"/></g></svg>
          <span>Telnova</span>
          <svg width="16" height="11" viewBox="0 0 16 11"><g fill="none" stroke="#fff" stroke-width="1.6"><path d="M1 4a10 10 0 0 1 14 0"/><path d="M3.5 6.5a6.5 6.5 0 0 1 9 0"/></g><circle cx="8" cy="9.2" r="1.6" fill="#fff"/></svg>
        </div>
        <span>11:59</span>
        <div class="status-right"><span>100%</span><span class="battery"></span></div>
      </div>
      <div class="nav">
        <svg width="14" height="28" viewBox="0 0 14 28"><path d="M13 1 1 14l12 13" fill="none" stroke="#fff" stroke-width="1.3"/></svg>
        <span class="brand">VERKO</span>
      </div>
    </header>

    <div class="section-title">Closed Work Orders</div>

    <div class="order" style="top:135px"><div class="order-line"><span>TH2236-A</span><span>SAR</span></div><div class="order-line"><span>2017-10-23</span><span>121</span></div></div>
    <div class="delete-btn" style="top:135px"><svg width="28" height="34" viewBox="0 0 28 34"><g fill="none" stroke="#fff" stroke-width="2"><rect x="10" y="1" width="8" height="4"/><path d="M2 6h24"/><path d="M4 9h20l-1.5 23h-17z"/><path d="M10 13v15M14 13v15M18 13v15"/></g></svg></div>

    <div class="order" style="top:214px"><div class="order-line"><span>TH2236-A</span><span>SAR</span></div><div class="order-line"><span>2017-10-23</span><span>121</span></div></div>
    <div class="delete-btn" style="top:214px"><svg width="28" height="34" viewBox="0 0 28 34"><g fill="none" stroke="#fff" stroke-width="2"><rect x="10" y="1" width="8" height="4"/><path d="M2 6h24"/><path d="M4 9h20l-1.5 23h-17z"/><path d="M10 13v15M14 13v15M18 13v15"/></g></svg></div>

    <div class="order" style="top:293px"><div class="order-line"><span>TH2236-A</span><span>SAR</span></div><div class="order-line"><span>2017-10-23</span><span>121</span></div></div>
    <div class="delete-btn" style="top:293px"><svg width="28" height="34" viewBox="0 0 28 34"><g fill="none" stroke="#fff" stroke-width="2"><rect x="10" y="1" width="8" height="4"/><path d="M2 6h24"/><path d="M4 9h20l-1.5 23h-17z"/><path d="M10 13v15M14 13v15M18 13v15"/></g></svg></div>

    <div class="order" style="top:372px"><div class="order-line"><span>TH2236-A</span><span>SAR</span></div><div class="order-line"><span>2017-10-23</span><span>121</span></div></div>
    <div class="delete-btn" style="top:372px"><svg width="28" height="34" viewBox="0 0 28 34"><g fill="none" stroke="#fff" stroke-width="2"><rect x="10" y="1" width="8" height="4"/><path d="M2 6h24"/><path d="M4 9h20l-1.5 23h-17z"/><path d="M10 13v15M14 13v15M18 13v15"/></g></svg></div>

    <div class="order" style="top:451px"><div class="order-line"><span>TH2236-A</span><span>SAR</span></div><div class="order-line"><span>2017-10-23</span><span>121</span></div></div>
    <div class="delete-btn" style="top:451px"><svg width="28" height="34" viewBox="0 0 28 34"><g fill="none" stroke="#fff" stroke-width="2"><rect x="10" y="1" width="8" height="4"/><path d="M2 6h24"/><path d="M4 9h20l-1.5 23h-17z"/><path d="M10 13v15M14 13v15M18 13v15"/></g></svg></div>

    <div class="list-end"></div>
    <div class="add-btn"><svg width="34" height="34" viewBox="0 0 34 34"><path d="M17 1v32M1 17h32" stroke="var(--plus-stroke)" stroke-width="2"/></svg></div>
  </main>
</body>
</html>
```